Business Card Design

Marla Quibbet
Artist of Contemporary/Modern/Representational Art
Contact: 0457219308
Please include my web site (thanks)! http://www.artvault913.com.au/marla-quibbet
And
Email: marlaquibbet@fernpost.example

Target Market(s)

Modern professional People who know what they like in modern contemporary art and have the means to purchase it.

Industry/Entity Type

Business

Contact Information for Business Card

Marla Quibbet
Contact: 0457219308

Font styles to use
Sans Serif

Requirements
Must have
• Simplicity & to the point
Keep the font modern/ contemporary
Nice to have
• A portrait of me and one piece of work on the business card (one on each side).
Should not have
• I'm not into butterflies.
No feminine style swirls
Nor I like swirls that look like tatoos

```html
<!DOCTYPE html>
<html lang="en">
<head>
<meta charset="utf-8">
<title>Marla Quibbet — Business Card</title>
<link rel="stylesheet" href="https://fonts.googleapis.com/css2?family=Anton&display=swap">
<style>
  :root {
    --backdrop: #eceae5;
    --card: #0b0b0b;
    --ink: #ffffff;
    --frame: #dcdad2;
    --frame-edge: #b9b6ac;
    --frame-inner: #f1efe8;
  }
  * { margin: 0; padding: 0; box-sizing: border-box; }
  html, body {
    width: 1200px;
    height: 848px;
    overflow: hidden;
    background: var(--backdrop);
  }
  .canvas {
    position: relative;
    width: 1200px;
    height: 848px;
    font-family: "Anton", "Impact", sans-serif;
    color: var(--ink);
  }
  .card {
    position: absolute;
    background: var(--card);
    overflow: hidden;
  }
  .card--front { left: 103px; top: 38px; width: 465px; height: 755px; }
  .card--back  { left: 607px; top: 34px; width: 466px; height: 755px; }

  .portrait {
    position: absolute;
    left: 0; top: 150px;
    width: 465px; height: 605px;
    background:
      radial-gradient(ellipse 55% 50% at 50% 50%, #7a5a4c 0%, #3a2b26 45%, rgba(11,11,11,0) 80%),
      radial-gradient(ellipse 60% 25% at 50% 92%, #b0402a 0%, rgba(11,11,11,0) 75%);
  }
  .name {
    position: absolute;
    left: 0; right: 0; top: 40px;
    text-align: center;
    font-size: 66px;
    font-weight: 400;
    line-height: 1;
    letter-spacing: 0.8px;
  }
  .phone {
    position: absolute;
    left: 0; right: 0; top: 145px;
    text-align: center;
    font-size: 34px;
    line-height: 1;
    letter-spacing: 0.8px;
  }
  .contact {
    position: absolute;
    left: 0; right: 0; top: 674px;
    text-align: center;
    font-size: 22px;
    line-height: 31px;
    letter-spacing: 0.5px;
  }

  .tagline {
    position: absolute;
    left: 0; right: 0; top: 294px;
    text-align: center;
    font-size: 40px;
    line-height: 53px;
    letter-spacing: 0.8px;
  }
  .artwork-frame {
    position: absolute;
    width: 190px;
    height: 157px;
    background: var(--frame);
    border: 3px solid var(--frame-edge);
    padding: 14px;
  }
  .artwork-frame__mat {
    width: 100%;
    height: 100%;
    border: 4px solid var(--frame-inner);
    outline: 2px solid var(--frame-edge);
  }
  .artwork {
    width: 100%;
    height: 100%;
  }
  .artwork--harbour { background: linear-gradient(160deg, #4a6f86, #c4552e 55%, #2b4e66); }
  .artwork--facades { background: linear-gradient(90deg, #c23a32, #d8b437 35%, #4c8ab0 65%, #5e9a4c); }
  .artwork--street  { background: linear-gradient(90deg, #d4a43c, #2b2b2b 40%, #d9475a 60%, #bfbfbf); }
  .artwork--city    { background: linear-gradient(170deg, #8c8f94, #4f7e3f 45%, #2e6f8e 70%, #3d6e33); }
</style>
</head>
<body>
<div class="canvas">

  <section class="card card--front">
    <div class="portrait" role="img" aria-label="Portrait photograph of the artist"></div>
    <h1 class="name">Marla Quibbet</h1>
    <p class="phone">0457219308</p>
    <p class="contact">
      marlaquibbet@fernpost.example<br>
      www.artvault913.com.au/marla-quibbet
    </p>
  </section>

  <section class="card card--back">
    <div class="artwork-frame" style="left:44px; top:108px;">
      <div class="artwork-frame__mat">
        <div class="artwork artwork--harbour" role="img" aria-label="Painting of a colourful harbour town"></div>
      </div>
    </div>
    <div class="artwork-frame" style="left:241px; top:67px;">
      <div class="artwork-frame__mat">
        <div class="artwork artwork--facades" role="img" aria-label="Painting of bright coloured building facades"></div>
      </div>
    </div>

    <p class="tagline">Artist of Contemporary<br>Modern<br>Representational Art</p>

    <div class="artwork-frame" style="left:44px; top:519px;">
      <div class="artwork-frame__mat">
        <div class="artwork artwork--street" role="img" aria-label="Painting of a street with bare trees and houses"></div>
      </div>
    </div>
    <div class="artwork-frame" style="left:241px; top:479px;">
      <div class="artwork-frame__mat">
        <div class="artwork artwork--city" role="img" aria-label="Painting of a city with a river and stadium"></div>
      </div>
    </div>
  </section>

</div>
</body>
</html>
```